Velqor5 Business Card - Health

Velqor5 maximizes value from the health data of its clients, including doctors, HMOs, and patients. I have attached the Velqor5 logo as an ai and eps file.
Target Market(s)
Health, HMO, Healthcare, Data, Big Data, Data Analytics
Industry/Entity Type
Business
Requirements
Must have
- At least one side should have some white on it so that we can write on it.

```html
<!DOCTYPE html>
<html lang="en">
<head>
<meta charset="utf-8">
<title>Velqor5 Business Card</title>
<link rel="stylesheet" href="https://fonts.googleapis.com/css2?family=Open+Sans:wght@400;600;700&display=swap">
<style>
  :root {
    --backdrop: #e4e4e4;
    --card-black: #111214;
    --card-black-edge: #1b1c1f;
    --brand-blue: #1e8fe8;
    --brand-blue-light: #14a6f0;
    --brand-blue-deep: #0a63c9;
    --write-white: #ffffff;
    --write-tint: #eaf6ff;
    --ink-white: #ffffff;
    --ink-dark: #0c1a2a;
  }
  html, body {
    margin: 0;
    padding: 0;
    width: 1200px;
    height: 1200px;
    overflow: hidden;
    background: var(--backdrop);
    font-family: "Open Sans", Arial, sans-serif;
  }
  .canvas {
    position: relative;
    width: 1200px;
    height: 1200px;
    display: flex;
    flex-direction: column;
    align-items: center;
    justify-content: center;
    gap: 70px;
  }
  .card {
    position: relative;
    width: 700px;
    height: 400px;
    border-radius: 22px;
    background: linear-gradient(135deg, var(--card-black-edge), var(--card-black) 60%);
    overflow: hidden;
    box-shadow: 0 10px 30px rgba(0, 0, 0, 0.18);
  }
  /* front */
  .card-front {
    display: flex;
    align-items: center;
    justify-content: center;
  }
  .brand {
    display: flex;
    align-items: center;
    gap: 26px;
  }
  .brand-dot {
    width: 70px;
    height: 70px;
    border-radius: 50%;
    background: var(--brand-blue);
  }
  .brand-name {
    color: var(--ink-white);
    font-weight: 400;
    font-size: 78px;
    letter-spacing: 1px;
    line-height: 1;
  }
  /* back */
  .info-panel {
    position: absolute;
    top: 30px;
    right: 60px;
    width: 500px;
    height: 340px;
    border-radius: 8px;
    background: linear-gradient(135deg, var(--brand-blue-light) 0%, var(--brand-blue) 55%, var(--brand-blue-deep) 100%);
  }
  .write-area {
    position: absolute;
    left: 70px;
    right: 70px;
    top: 50px;
    bottom: 50px;
    border-radius: 6px;
    background: linear-gradient(180deg, var(--write-white), var(--write-tint));
    display: flex;
    flex-direction: column;
    align-items: center;
    justify-content: center;
    color: var(--ink-dark);
    text-align: center;
  }
  .person-name {
    margin: 0;
    font-size: 26px;
    font-weight: 700;
    letter-spacing: 0.5px;
    line-height: 1.2;
  }
  .person-title {
    margin: 2px 0 26px;
    font-size: 13px;
    font-weight: 400;
  }
  .contact-list {
    list-style: none;
    margin: 0;
    padding: 0;
    font-size: 16px;
    line-height: 1.5;
  }
</style>
</head>
<body>
  <main class="canvas">
    <section class="card card-front" aria-label="Card front">
      <div class="brand">
        <span class="brand-dot"></span>
        <span class="brand-name">Velqor5</span>
      </div>
    </section>

    <section class="card card-back" aria-label="Card back">
      <div class="info-panel" role="img" aria-label="Blue faceted decorative panel behind the contact details">
        <div class="write-area">
          <h1 class="person-name">Your name</h1>
          <p class="person-title">Your Title</p>
          <ul class="contact-list">
            <li>+00 111 222 3333</li>
            <li>yourname@yourwebsite.com</li>
            <li>www.yourwebsite.com</li>
          </ul>
        </div>
      </div>
    </section>
  </main>
</body>
</html>
```